Talvex Engineering Business card Design

We need to make business cards for our NDT and inspection company. The company is called Talvex Engineering. We want a professional modern feel business card. We have just completed the remaking of our website and would like to have business cards with the same feel and colours. The final design should communicate professionalism and cutting edge tech.

Target Market(s)

We sell to B2B Business clients. Our customer is an engineer or decision maker in the mechanical engineering / Oil and gas field.

Contact Information for Business Card

Please see the current business cards that we have uploaded to get the details. You can also look at our Website www.talvex-eng.example for more.

Requirements
Must have
• Less is more
Nice to have
• Less is more

```html
<!DOCTYPE html>
<html lang="en">
<head>
<meta charset="utf-8">
<title>Talvex Engineering – Business Card</title>
<link href="https://fonts.googleapis.com/css2?family=Roboto:wght@400;500;700&display=swap" rel="stylesheet">
<style>
  :root {
    --backdrop: #2e2420;
    --navy: #1f2d63;
    --red: #a8202a;
    --white: #ffffff;
    --rule: #8d97bd;
    --ring: #9a9ca4;
  }
  * { margin: 0; padding: 0; box-sizing: border-box; }
  html, body { width: 1200px; height: 716px; overflow: hidden; }
  body {
    background: var(--backdrop);
    font-family: "Roboto", Arial, sans-serif;
    position: relative;
  }
  .card {
    position: absolute;
    top: 203px;
    width: 540px;
    height: 310px;
    border-radius: 4px;
    box-shadow: 0 10px 28px rgba(0,0,0,.45);
  }
  /* Back side */
  .card--back { left: 30px; background: var(--navy); color: var(--white); }
  .card--back .brand {
    position: absolute; left: 30px; top: 92px; width: 210px;
    display: flex; align-items: center; gap: 12px;
  }
  .brand__dot {
    flex: none; width: 22px; height: 22px; border-radius: 50%;
    background: var(--white);
  }
  .brand__name { font-size: 22px; font-weight: 500; line-height: 1.15; }
  .card--back .divider {
    position: absolute; left: 262px; top: 44px; width: 1px; height: 200px;
    background: var(--rule);
  }
  .services {
    position: absolute; left: 284px; top: 44px; list-style: none;
    font-size: 12.5px; line-height: 17px;
  }
  .services li { position: relative; padding-left: 12px; }
  .services li::before {
    content: ""; position: absolute; left: 0; top: 6px;
    width: 5px; height: 5px; border-radius: 50%; background: var(--red);
  }
  .card--back .website {
    position: absolute; left: 30px; bottom: 40px; font-size: 13px;
  }
  /* Front side */
  .card--front { left: 630px; background: var(--white); color: var(--navy); }
  .card--front .brand {
    position: absolute; left: 28px; top: 118px; width: 220px;
    display: flex; align-items: center; gap: 12px;
  }
  .card--front .brand__dot { background: var(--red); }
  .card--front .brand__name { color: var(--navy); }
  .card--front .divider {
    position: absolute; left: 268px; top: 60px; width: 1px; height: 190px;
    background: var(--navy);
  }
  .contact { position: absolute; left: 290px; top: 62px; font-size: 14px; }
  .contact__name { color: var(--red); font-size: 22px; font-weight: 700; }
  .contact__role { font-size: 16px; margin-bottom: 10px; }
  .contact__address { line-height: 18px; margin-bottom: 10px; }
  .contact__line { display: flex; align-items: center; gap: 8px; line-height: 20px; }
  .contact__line svg { width: 12px; height: 12px; flex: none; }
  .accent { color: var(--red); }
</style>
</head>
<body>
  <section class="card card--back">
    <div class="brand"><span class="brand__dot"></span><span class="brand__name">Talvex Engineering</span></div>
    <div class="divider"></div>
    <ul class="services">
      <li>API 653 Tank Inspections</li>
      <li>API 570 Pipeline Inspections</li>
      <li>API 510 Pressure Vessel Inspections</li>
      <li>Welding Inspection</li>
      <li>Electrical Inspection</li>
      <li>OCTG Inspections</li>
      <li>Lifting Equipment Inspections</li>
      <li>Non-Destructive Testing</li>
      <li>UT / PT / MT / RT / VT</li>
      <li>Advanced NDT</li>
      <li>PAUT / MFL / ILI</li>
      <li>Engineering Projects</li>
    </ul>
    <div class="website">www.talvex-eng.example</div>
  </section>

  <section class="card card--front">
    <div class="brand"><span class="brand__dot"></span><span class="brand__name">Talvex Engineering</span></div>
    <div class="divider"></div>
    <div class="contact">
      <div class="contact__name">Daniel Mwangi</div>
      <div class="contact__role">Manager</div>
      <div class="contact__address">P.O. BOX 40312-80100<br>Kilifi Kenya</div>
      <div class="contact__line">
        <svg viewBox="0 0 12 12" aria-hidden="true"><path d="M2.5 1l2 2.2-1 1.3a6 6 0 0 0 4 4l1.3-1 2.2 2-1.2 1.5C5.5 11 1 6.5 1 2.2z" fill="#a8202a"/></svg>
        <span>+ 254 20 555 0142/3</span>
      </div>
      <div class="contact__line">
        <svg viewBox="0 0 12 12" aria-hidden="true"><rect x="1" y="2.5" width="10" height="7" fill="none" stroke="#a8202a" stroke-width="1.2"/><path d="M1 2.5l5 4 5-4" fill="none" stroke="#a8202a" stroke-width="1.2"/></svg>
        <span>info@talvex-eng.example</span>
      </div>
      <div class="contact__line">
        <svg viewBox="0 0 12 12" aria-hidden="true"><circle cx="6" cy="6" r="5" fill="none" stroke="#a8202a" stroke-width="1.2"/><path d="M1 6h10M6 1c-2.5 3-2.5 7 0 10M6 1c2.5 3 2.5 7 0 10" fill="none" stroke="#a8202a" stroke-width="1"/></svg>
        <span>www.<span class="accent">talvex-eng</span>.example</span>
      </div>
    </div>
  </section>
</body>
</html>
```